Redesign website for small print company

Vindaborgprent is a small printing company in Iceland mainly servicing Students, schools, etc. We are also doing all kind of other jobs, like business cards, book printing, brochure printing etc. We are also selling books online.
Our website is: www.vindaborgprent.is
What we are looking for is:
- Web Design (Uncoded - PSD layout only)
- Mobile friendly design, using our current color scheme: Red, green, yellow and light gray.
- Clean simple design
- Simple, light and easy to use.
- More menu Items/drop down
Industry/Entity Type
Digital Printing
Number of Pages Required
5+ page
Requirements
Must have
- Easy navigation
- Designed for mobile
- Current color scheme (see logo)
Nice to have
- Icon based products

```html
<!DOCTYPE html>
<html lang="is">
<head>
<meta charset="utf-8">
<title>Vindaborgprent</title>
<link href="https://fonts.googleapis.com/css2?family=Montserrat:ital,wght@0,300;0,400;0,500;0,600;0,700;0,800;1,600&display=swap" rel="stylesheet">
<style>
:root{
  --red:#e8242b;
  --green:#27b36a;
  --yellow:#f7cf1e;
  --ink:#151515;
  --text:#3a3a3a;
  --muted:#8a8a8a;
  --panel:#f4f4f4;
  --panel-2:#ececec;
  --line:#e2e2e2;
  --white:#ffffff;
  --dark-badge:#2b2b2b;
}
*{box-sizing:border-box;margin:0;padding:0}
html,body{width:1200px;height:2748px;overflow:hidden}
body{background:var(--white);font-family:"Montserrat",Arial,sans-serif;color:var(--text);position:relative}
section,header,footer{position:absolute;left:0;width:1200px}

/* header */
.site-header{top:0;height:76px;border-bottom:1px solid var(--line);display:flex;align-items:center;padding:0 92px}
.brand{display:flex;align-items:center;gap:8px;font-weight:800;font-size:20px;color:var(--ink);letter-spacing:.2px}
.brand-square{width:18px;height:18px;background:var(--red)}
.main-nav{display:flex;gap:40px;margin-left:auto;margin-right:54px;height:76px;align-items:center}
.main-nav a{font-size:12px;font-weight:700;color:var(--ink);text-decoration:none;height:76px;display:flex;align-items:center;border-bottom:3px solid transparent}
.main-nav a.active{border-bottom-color:var(--green)}
.header-tools{display:flex;gap:16px;align-items:center;margin-right:40px}

/* hero */
.hero{top:76px;height:400px}
.hero-copy{position:absolute;left:72px;top:62px;width:580px;z-index:2}
.hero-title{font-size:40px;line-height:1.1;color:var(--ink);font-weight:400;white-space:nowrap}
.hero-title strong{font-weight:700;display:block}
.hero-text{font-size:14px;line-height:1.6;margin-top:16px;color:var(--text);width:370px}
.btn-red{display:inline-block;background:var(--red);color:var(--white);font-size:13px;font-weight:600;padding:12px 26px;margin-top:26px;border-radius:3px}
.hero-visual{position:absolute;left:522px;top:0;width:678px;height:400px;background:linear-gradient(150deg,#f7f7f7 0%,#c9ccd4 35%,#3d4f74 60%,#e9e6e0 80%,#f5f5f5 100%)}
.slider-dots{position:absolute;left:550px;top:350px;display:flex;gap:6px;z-index:2}
.slider-dots span{width:12px;height:12px;border-radius:50%;background:#d3d3d3}
.slider-dots span.on{background:#8c8c8c}

/* advantages */
.advantages{top:476px;height:370px;display:flex}
.adv-lead{width:600px;background:var(--panel);padding:78px 0 0 116px}
.adv-lead h2{font-size:27px;font-weight:700;line-height:1.42;color:var(--ink);width:350px;letter-spacing:.3px}
.adv-lead h2 em{font-style:normal;color:var(--green)}
.adv-quote{width:600px;background:var(--panel-2);position:relative;padding:80px 0 0 110px}
.adv-quote blockquote{font-size:14px;font-style:italic;font-weight:600;color:var(--muted);line-height:1.95;width:345px}
.quote-author{margin-top:16px;font-size:12px;color:var(--ink);font-weight:700}
.quote-author span{display:block;font-weight:400;font-size:11px;color:var(--text)}
.quote-mark{position:absolute;left:390px;top:242px}
.quote-dots{position:absolute;left:110px;top:318px;display:flex;gap:8px}
.quote-dots span{width:7px;height:7px;border-radius:50%;background:#cfcfcf}
.quote-dots span.on{background:var(--red)}

/* services */
.services{top:846px;height:504px;display:grid;grid-template-columns:repeat(4,300px);grid-template-rows:252px 252px}
.tile{position:relative;overflow:hidden}
.tile-photo{position:absolute;inset:0}
.tile-enlarge{grid-column:1/3;grid-row:1}
.tile-magnets{grid-column:3;grid-row:1;background:var(--red);color:var(--white);padding:28px 24px 0 50px;text-align:right}
.tile-notebook{grid-column:4;grid-row:1/3}
.tile-calendar{grid-column:1;grid-row:2}
.tile-folder{grid-column:2;grid-row:2}
.tile-envelopes{grid-column:3;grid-row:2}
.badge{position:absolute;right:0;top:40px;font-size:14px;font-weight:700;line-height:1.2;padding:7px 10px;text-align:right;color:var(--white)}
.badge-green{background:var(--green)}
.badge-red{background:var(--red)}
.badge-yellow{background:var(--yellow);color:var(--white)}
.badge-dark{background:var(--dark-badge)}
.tile-magnets h3{font-size:18px;font-weight:500}
.tile-magnets h3 b{font-weight:700}
.tile-magnets p{font-size:12px;font-weight:600;line-height:1.75;margin-top:14px}
.btn-outline{display:inline-block;margin-top:16px;border:1px solid rgba(255,255,255,.8);font-size:12px;font-weight:600;padding:8px 28px}

/* welcome */
.welcome{top:1350px;height:675px;text-align:center}
.welcome h2{font-size:29px;font-weight:700;color:var(--ink);margin-top:44px}
.welcome-intro{font-size:15px;font-weight:500;color:var(--ink);line-height:1.7;width:830px;margin:12px auto 0}
.welcome-body{font-size:11px;line-height:2.4;color:var(--text);width:900px;margin:18px auto 0}
.welcome-visual{position:absolute;left:135px;top:280px;width:930px;height:340px;background:radial-gradient(ellipse at center,#e7c9a8 0%,#d9664d 30%,#4a72a8 55%,#ffffff 78%)}

/* map */
.location-map{top:2025px;height:325px;background:linear-gradient(160deg,#a9cdea 0%,#b9d7ee 40%,#e8ece6 55%,#dfe9d6 100%)}
.map-pin{position:absolute;left:775px;top:118px}

/* newsletter */
.newsletter{top:2350px;height:100px;display:flex;align-items:center;padding:0 0 0 133px}
.newsletter-title{font-size:16px;font-weight:600;color:var(--ink);line-height:1.2;width:305px}
.newsletter-title b{display:block;color:var(--red);font-weight:700;font-size:17px}
.field{width:160px;height:38px;border:1px solid #d5d5d5;font-size:11px;color:var(--text);display:flex;align-items:center;padding-left:10px;margin-right:18px}
.field-wide{width:262px;margin-right:45px}
.btn-subscribe{background:var(--red);color:var(--white);font-size:12px;font-weight:700;width:138px;height:38px;display:flex;align-items:center;justify-content:center;border-radius:2px}

/* footer */
.site-footer{top:2450px;height:190px}
.footer-brand{position:absolute;left:133px;top:46px}
.footer-brand .brand{font-size:17px}
.contact-list{list-style:none;margin-top:12px;font-size:11px;color:var(--ink);line-height:2}
.contact-list li{display:flex;align-items:center;gap:8px}
.footer-col{position:absolute;top:36px}
.footer-col h4{font-size:14px;font-weight:700;margin-bottom:8px}
.footer-col ul{list-style:none;font-size:11px;color:var(--ink);line-height:1.9}
.col-about{left:404px}.col-about h4{color:var(--red)}
.col-account{left:670px}.col-account h4{color:var(--green)}
.col-inclusion{left:920px}.col-inclusion h4{color:var(--yellow)}
.footer-bar{position:absolute;left:133px;top:2664px;width:934px;border-top:1px solid var(--line);display:flex;justify-content:space-between;align-items:center;padding-top:14px;font-size:10px;color:var(--ink)}
.social{display:flex;gap:6px}
.social span{width:16px;height:16px;border-radius:50%;border:1px solid #555}
.social span.hot{border-color:var(--red);background:var(--red)}
</style>
</head>
<body>

<header class="site-header">
  <div class="brand"><span class="brand-square"></span>VINDABORGPRENT</div>
  <nav class="main-nav">
    <a href="#">HEIM</a>
    <a href="#" class="active">ÞJÓNUSTA</a>
    <a href="#">SKIL Á VERKUM</a>
    <a href="#">UM OKKUR</a>
  </nav>
  <div class="header-tools">
    <svg width="26" height="24" viewBox="0 0 26 24" aria-label="Cart"><path d="M1 3h4l3 12h12l3-9H7" fill="none" stroke="#151515" stroke-width="2"/><circle cx="10" cy="20" r="2" fill="#151515"/><circle cx="19" cy="20" r="2" fill="#151515"/><circle cx="22" cy="4" r="4" fill="#f7cf1e"/></svg>
    <svg width="22" height="22" viewBox="0 0 22 22" aria-label="Search"><circle cx="9" cy="9" r="7" fill="none" stroke="#151515" stroke-width="2.2"/><path d="M14 14l6 6" stroke="#151515" stroke-width="2.4"/></svg>
  </div>
</header>

<section class="hero">
  <div class="hero-visual" role="img" aria-label="Printed brochures, business cards and stationery laid out at an angle"></div>
  <div class="hero-copy">
    <h1 class="hero-title">Here Write <strong>Your Polished Headline</strong></h1>
    <p class="hero-text">Lorem ipsum dolor sit amet, consectetuer adipiscing elit. Aenean commodo ligula eget dolor. Aenean massa sit amet adipiscing.</p>
    <span class="btn-red">Get in Touch</span>
  </div>
  <div class="slider-dots"><span></span><span></span><span></span><span class="on"></span><span></span></div>
</section>

<section class="advantages">
  <div class="adv-lead">
    <h2>Here you should have an <em>eye caching</em> text with mentioning about your company advantages</h2>
  </div>
  <div class="adv-quote">
    <blockquote>Lorem ipsum dolor sit amet, consectetuer adipiscing elit. Aenean commodo ligula eget dolor. Aenean massa. Cum sociis natoque penatibus et magnis dis parturient montes, nascetur ridiculus mus. Donec quam felis, ultricies nec, pellentesque eu, pretium quis, sem.</blockquote>
    <div class="quote-author">Jon Arnason —<span>Company CEO</span></div>
    <svg class="quote-mark" width="80" height="64" viewBox="0 0 80 64"><path d="M4 64V34C4 14 14 4 32 0v12c-9 3-13 9-13 18h13v34zM46 64V34C46 14 56 4 74 0v12c-9 3-13 9-13 18h13v34z" fill="#dcdcdc"/></svg>
    <div class="quote-dots"><span></span><span class="on"></span><span></span><span></span><span></span></div>
  </div>
</section>

<section class="services">
  <div class="tile tile-enlarge">
    <div class="tile-photo" role="img" aria-label="Hand holding an enlarged landscape photo print" style="background:linear-gradient(120deg,#e9e4dc,#c8b8a0 45%,#6d6a63 75%,#2f2f2f)"></div>
    <span class="badge badge-green">Enlarge<br>Images</span>
  </div>
  <div class="tile tile-magnets">
    <h3>Print of <b>Magnets</b></h3>
    <p>Lorem ipsum dolor sit amet, consectetuer adipiscing elit. Aenean commodo ligula eget dolor. Aenean massa. ridiculus mus. Donec quam felis, ultricies nec. pellentesque eu. p</p>
    <span class="btn-outline">View Service</span>
  </div>
  <div class="tile tile-notebook">
    <div class="tile-photo" role="img" aria-label="Navy and pink notebooks with pencils on a light blue desk" style="background:linear-gradient(160deg,#cfe2ea,#aed2e0 40%,#1f2b44 60%,#f1b3ae 80%,#cfe2ea)"></div>
    <span class="badge badge-yellow">Notebook<br>Design</span>
  </div>
  <div class="tile tile-calendar">
    <div class="tile-photo" role="img" aria-label="Printed desk calendar" style="background:linear-gradient(140deg,#f2f2f2,#d9d9d9 50%,#3a3a3a 80%,#e86a9a)"></div>
    <span class="badge badge-red">Calendar<br>Design</span>
  </div>
  <div class="tile tile-folder">
    <div class="tile-photo" role="img" aria-label="Dark branded presentation folders" style="background:linear-gradient(150deg,#1d2330,#2d3a52 50%,#e05a2a 75%,#1a1a1a)"></div>
    <span class="badge badge-yellow">Folder<br>Design</span>
  </div>
  <div class="tile tile-envelopes">
    <div class="tile-photo" role="img" aria-label="Printed envelopes with blue branding" style="background:linear-gradient(150deg,#d6e8f5,#f6f8fa 45%,#2a6bd1 70%,#a8c9ec)"></div>
    <span class="badge badge-dark">Printing<br>Envelopes</span>
  </div>
</section>

<section class="welcome">
  <h2>Velkomin í Vindaborgprent</h2>
  <p class="welcome-intro">Vindaborgprent er fyrirtæki staðsett á háskólasvæðinu sem hefur sérhæft sig í að þjónusta skólafólk, ásamt því að sinna allri almennri prentun fyrir almenning.</p>
  <p class="welcome-body">Vindaborgprent gefur út greinasöfn og frumsamdar kennslubækur fyrir námskeið, prentar lokaritgerðir fyrir nema, auk þess að vinna við ótalinn fjölda smærri verka fyrir nemendur, kennara og starfsmenn. Má þar nefna bæklinga, skýrslur, spurningalista, nafnspjöld, bækur, OCR skönnun og fleira. Vindaborgprent er umhverfisvottuð prentsmiðja. Vottunin er opinbert umhverfismerki sem hefur skapað sér fótfestu hér á landi og er þekkt meðal neytenda. Vindaborgprent er staðsett á horninu á Hrafnagötu og Vesturgötu (gengið inn Vesturgötumegin)</p>
  <div class="welcome-visual" role="img" aria-label="Row of cheerful schoolchildren jumping with backpacks"></div>
</section>

<section class="location-map" role="img" aria-label="Street map of the area around the print shop">
  <svg class="map-pin" width="22" height="32" viewBox="0 0 22 32"><path d="M11 0C5 0 0 5 0 11c0 8 11 21 11 21s11-13 11-21C22 5 17 0 11 0z" fill="#e8242b"/><circle cx="11" cy="11" r="4" fill="#8f1014"/></svg>
</section>

<section class="newsletter">
  <div class="newsletter-title">Subscribe<b>For Our Newsletter</b></div>
  <div class="field">Full Name..</div>
  <div class="field field-wide">Email Address..</div>
  <div class="btn-subscribe">Subscribe</div>
</section>

<footer class="site-footer">
  <div class="footer-brand">
    <div class="brand"><span class="brand-square"></span>VINDABORGPRENT</div>
    <ul class="contact-list">
      <li><svg width="12" height="12" viewBox="0 0 12 12"><path d="M2 1l2 0 1 3-1.5 1a7 7 0 0 0 3.5 3.5L8 7l3 1v2c0 1-1 1-1 1C5 11 1 7 1 2c0 0 0-1 1-1z" fill="#e8242b"/></svg>+354 555 0142</li>
      <li><svg width="12" height="10" viewBox="0 0 12 10"><rect width="12" height="10" fill="#e8242b"/><path d="M0 0l6 5 6-5" fill="none" stroke="#fff"/></svg>info@inkora-mail.com</li>
      <li style="padding-left:20px">Company Name</li>
    </ul>
  </div>
  <div class="footer-col col-about"><h4>About Inkora</h4><ul><li>Newsletter</li><li>Our Memberships</li><li>Events</li><li>Investors</li><li>Suppliers Response</li></ul></div>
  <div class="footer-col col-account"><h4>Account</h4><ul><li>Manage Your ID</li><li>Inkora Store</li><li>Customer Reveiws</li><li>Ask a Question</li><li>Why choose us?</li></ul></div>
  <div class="footer-col col-inclusion"><h4>Inclusion</h4><ul><li>Inclusion and Diversity</li><li>Supplier Responsibility</li><li>Inclusion and Diversity</li><li>Shop for Business</li><li>Shop for Consumers</li></ul></div>
</footer>

<div class="footer-bar">
  <span>Copyright 2018 Inkora | All rights reserved</span>
  <div class="social"><span></span><span class="hot"></span><span></span></div>
</div>

</body>
</html>
```